K & D A/C Compressors' Business Card

Hello,

I need someone to create a new business card for my business. The name of my Business is: K & D A/C Compressors. I sell automotive air conditioning parts (a/c parts). I would like the business card to incorporate my logo, and to have an automotive feel to it. It is important that the business card feel like it is coming from an automotive parts business.

I already have a logo, which I will provide.

Thanks.
Updates

Project Deadline Extended Reason: I feel like extending the deadline until October 9, 2017, will allow for more time to design the business card. Thank you for your understanding. Added Monday, October 2, 2017

Target Market(s)

Consumers who need automotive a/c parts, and auto mechanics.

Industry/Entity Type

Automotive

Contact Information for Business Card

Business name: K & D A/C Compressors
Business Address: 48207 Southwest 36th Street, Palm Reef, Florida 33490
Telephone: 305-472-1390
Fax: To be provided once I choose your design.
Website: www.kdcoolunits.example
Email: support@kdcoolunits.example
Names: To be provided once I choose your design.

Font styles to use
Sans Serif

Colors

Designer to choose colors to be used in the design.

Requirements
Must have
• The business card must include all of the "Business Card Details" and the logo I have uploaded.

```html
<!DOCTYPE html>
<html lang="en">
<head>
<meta charset="utf-8">
<title>K &amp; D A/C Compressors – Business Card</title>
<link rel="stylesheet" href="https://fonts.googleapis.com/css2?family=Open+Sans:wght@300;400;700&display=swap">
<style>
  :root {
    --stage: #1c1c1c;
    --paper: #ffffff;
    --brand-blue: #00a9ec;
    --steel-grey: #a6a7aa;
    --logo-grey: #9b9c9f;
    --ink: #2e2e2e;
  }
  * { box-sizing: border-box; margin: 0; padding: 0; }
  html, body { width: 1200px; height: 900px; overflow: hidden; background: var(--stage); }
  body { position: relative; font-family: "Open Sans", Arial, sans-serif; }

  .card {
    position: absolute;
    top: 306px;
    width: 440px;
    height: 271px;
    box-shadow: 2px 3px 4px rgba(0,0,0,0.55);
    overflow: hidden;
  }
  .card-front { left: 149px; background: var(--paper); }
  .card-back { left: 608px; background: var(--brand-blue); }

  .front-accent { position: absolute; left: 0; top: 26px; }
  .holder { position: absolute; left: 35px; top: 31px; }
  .holder-name { color: var(--brand-blue); font-weight: 700; font-size: 16px; line-height: 19px; letter-spacing: 0.2px; }
  .holder-title { color: var(--ink); font-size: 12px; line-height: 14px; }

  .brand-name {
    position: absolute; right: 24px; top: 86px;
    text-align: right; color: var(--logo-grey); font-weight: 300;
  }
  .brand-name .brand-initials { display: block; font-size: 40px; line-height: 44px; }
  .brand-name .brand-line { display: block; font-size: 21px; line-height: 26px; }

  .contact-list { position: absolute; left: 28px; top: 174px; list-style: none; }
  .contact-list li { display: flex; align-items: center; height: 16px; font-size: 12px; color: var(--ink); }
  .contact-list svg { width: 10px; height: 10px; margin-right: 6px; fill: var(--brand-blue); flex: none; }

  .address {
    position: absolute; right: 23px; top: 205px;
    text-align: right; font-size: 12px; line-height: 16px; color: var(--ink); font-style: normal;
  }
  .front-band { position: absolute; left: 0; bottom: 0; }

  .back-pattern { position: absolute; inset: 0; background: var(--brand-blue); }
  .back-name {
    position: absolute; left: 250px; top: 158px;
    color: var(--paper); font-size: 11px; font-weight: 400; white-space: nowrap;
  }
</style>
</head>
<body>

<section class="card card-front" aria-label="Business card front">
  <svg class="front-accent" width="30" height="38" viewBox="0 0 30 38" aria-hidden="true">
    <polygon points="0,0 11,0 16,37 0,37" fill="var(--steel-grey)"/>
    <polygon points="11,0 28,0 28,37 16,37" fill="var(--brand-blue)"/>
  </svg>

  <div class="holder">
    <p class="holder-name">MARCUS ELLERY</p>
    <p class="holder-title">Managing Director</p>
  </div>

  <p class="brand-name">
    <span class="brand-initials">K &amp; D</span>
    <span class="brand-line">A/C Compressors</span>
  </p>

  <ul class="contact-list">
    <li><svg viewBox="0 0 10 10" aria-hidden="true"><path d="M2 0.5 L3.6 2.8 L2.7 3.8 Q3.8 6.2 6.2 7.3 L7.2 6.4 L9.5 8 L8.4 9.6 Q1.5 8.5 0.4 1.6 Z"/></svg>305-472-1390</li>
    <li><svg viewBox="0 0 10 10" aria-hidden="true"><rect x="2.5" y="0.5" width="5" height="3"/><rect x="0.5" y="3.5" width="9" height="5" rx="1"/><rect x="2.5" y="6.5" width="5" height="3" fill="#fff"/></svg>305-472-1390</li>
    <li><svg viewBox="0 0 10 10" aria-hidden="true"><circle cx="5" cy="5" r="4.6"/><path d="M1 5 H9 M5 0.6 Q2.5 5 5 9.4 M5 0.6 Q7.5 5 5 9.4" stroke="#fff" stroke-width="0.7" fill="none"/></svg>www.kdcoolunits.example</li>
    <li><svg viewBox="0 0 10 10" aria-hidden="true"><rect x="0.5" y="2" width="9" height="6.5"/><path d="M0.8 2.3 L5 5.6 L9.2 2.3" stroke="#fff" stroke-width="0.8" fill="none"/></svg>support@kdcoolunits.example</li>
  </ul>

  <address class="address">48207 Southwest 36th Street,<br>Palm Reef, Florida 33490</address>

  <svg class="front-band" width="440" height="15" viewBox="0 0 440 15" aria-hidden="true">
    <polygon points="0,0 218,0 206,15 0,15" fill="var(--steel-grey)"/>
    <polygon points="222,0 440,0 440,15 209,15" fill="var(--brand-blue)"/>
  </svg>
</section>

<section class="card card-back" aria-label="Business card back">
  <div class="back-pattern" role="img" aria-label="Repeating brand pattern in light blue tones"></div>
  <p class="back-name">K &amp; D A/C Compressors</p>
</section>

</body>
</html>
```